Business Card Design

I do estate sales and would like business card to reflect look and feel of attached logo. I also have copy of logo in .eps and .tif if you need that instead of .jpeg.
Updates

sorry for the delay in reviewing these designs. I will pick one by tomorrow. Here are the absolutes: *must have tagline (we find good homes for your treasures *must use blue and green *must be horizontal *nothing too fancy please submit your best and final. Thanks so much!

Industry/Entity Type

Business

Contact Information for Business Card

Nora Platt

DEALS by NORA
We find good homes for your treasures.

Specializing in one to three-day sales
o (no sale too big or too small)
• Home and garage organizing
• Home Clean-out

Call Nora Platt at 202-555-0187
to schedule.

```html
<!DOCTYPE html>
<html lang="en">
<head>
<meta charset="utf-8">
<title>DEALS by NORA – Business Card</title>
<link rel="stylesheet" href="https://fonts.googleapis.com/css2?family=Cabin:ital,wght@0,400;0,500;0,700;1,400;1,500;1,700&display=swap">
<style>
  :root {
    --teal: #12809f;
    --green: #6b8a3a;
    --rule: #3f8aa6;
    --paper: #ffffff;
  }
  * { margin: 0; padding: 0; box-sizing: border-box; }
  html, body {
    width: 1200px;
    height: 704px;
    overflow: hidden;
    background: var(--paper);
  }
  .card {
    position: relative;
    width: 1200px;
    height: 704px;
    background: var(--paper);
    font-family: "Cabin", "Gill Sans", sans-serif;
    overflow: hidden;
  }
  .band {
    position: absolute;
    left: 0;
    width: 1200px;
    background: var(--teal);
  }
  .band--top { top: 0; height: 31px; }
  .band--bottom { bottom: 0; height: 42px; }

  .frame-lines {
    position: absolute;
    left: 0;
    top: 0;
    width: 1200px;
    height: 704px;
  }

  .wordmark {
    position: absolute;
    left: 388px;
    top: 31px;
    width: 425px;
    height: 345px;
    display: flex;
    flex-direction: column;
    align-items: center;
    justify-content: center;
    color: var(--green);
    font-weight: 500;
    line-height: 1;
    text-align: center;
  }
  .wordmark__word { font-size: 96px; letter-spacing: 2px; }
  .wordmark__joiner { font-size: 54px; margin: 6px 0 10px; }

  .owner-name {
    position: absolute;
    left: 388px;
    top: 398px;
    width: 425px;
    text-align: center;
    color: var(--teal);
    font-weight: 700;
    font-size: 47px;
    letter-spacing: 1.5px;
    line-height: 1;
  }

  .line {
    position: absolute;
    left: 0;
    width: 1200px;
    text-align: center;
    color: var(--green);
    font-style: italic;
    line-height: 1;
  }
  .tagline { top: 484px; font-size: 29px; font-weight: 700; }
  .services { top: 540px; font-size: 20px; font-weight: 400; }
  .note { top: 583px; font-size: 18px; font-weight: 400; }
  .call { top: 619px; font-size: 36px; font-weight: 700; }
</style>
</head>
<body>
  <div class="card">
    <div class="band band--top"></div>

    <svg class="frame-lines" viewBox="0 0 1200 704" aria-hidden="true">
      <line x1="388" y1="31" x2="388" y2="461" stroke="var(--rule)" stroke-width="1"/>
      <line x1="813" y1="31" x2="813" y2="461" stroke="var(--rule)" stroke-width="1"/>
      <line x1="302" y1="377" x2="900" y2="377" stroke="var(--rule)" stroke-width="1"/>
    </svg>

    <div class="wordmark" aria-label="DEALS by NORA">
      <span class="wordmark__word">DEALS</span>
      <span class="wordmark__joiner">by</span>
      <span class="wordmark__word">NORA</span>
    </div>

    <div class="owner-name">NORA PLATT</div>

    <p class="line tagline">We find good homes for your treasures</p>
    <p class="line services">Specializing in one to three-day sales • Home and garage organizing • Home clean-out</p>
    <p class="line note">(no sale too big or too small)</p>
    <p class="line call">Call Nora Platt at 202-555-0187 to schedule</p>

    <div class="band band--bottom"></div>
  </div>
</body>
</html>
```